Ferncrest Dental, LLC business card project

Business card to be designed with current logo.
Dental office- please keep design of card that looks clean and professional.
Please include the following info:
Ferncrest Dental, LLC
Dr. Lorna Pettigrew
2871 Marlowe Street
Bethlehem, PA 18093
610-555-0193
ferncrestdental.office@examplemail.test
Hello everyone-
Reason: Just got back from overseas- will look at all designs and provide feedback. Thank you!
Reason: Polling my friends for the final selection-
thank you to all those that participated- so many talented designers!

```html
<!DOCTYPE html>
<html lang="en">
<head>
<meta charset="utf-8">
<title>Ferncrest Dental, LLC — Business Card</title>
<link rel="stylesheet" href="https://fonts.googleapis.com/css2?family=Arimo:wght@400&display=swap">
<style>
  :root {
    --page: #ffffff;
    --card: #ffffff;
    --card-edge: #d9d9d9;
    --green-dark: #5f9a3c;
    --green-light: #a9d033;
    --text-green: #3f7d3a;
    --text-dark: #111111;
  }
  * { box-sizing: border-box; margin: 0; padding: 0; }
  html, body { width: 1200px; height: 900px; overflow: hidden; background: var(--page); }
  body { position: relative; font-family: "Arimo", Arial, sans-serif; }

  .card {
    position: absolute;
    width: 580px;
    height: 330px;
    background: var(--card);
    border: 1px solid var(--card-edge);
    box-shadow: 3px 4px 8px rgba(0,0,0,0.35);
    overflow: hidden;
  }
  .card--back  { left: 490px; top: 90px; }
  .card--front { left: 130px; top: 480px; }

  .brand-name {
    position: absolute;
    font-size: 30px;
    font-weight: 400;
    color: var(--green-dark);
    letter-spacing: -0.5px;
    white-space: nowrap;
    display: flex;
    align-items: center;
    gap: 10px;
  }
  .brand-dot {
    width: 16px; height: 16px;
    border-radius: 50%;
    background: var(--green-light);
  }
  .card--back .brand-name { left: 100px; top: 70px; }
  .card--front .brand-name { left: 110px; top: 140px; font-size: 36px; }

  .address, .contact {
    position: absolute;
    font-size: 13px;
    line-height: 19px;
    color: var(--text-green);
    font-style: normal;
    white-space: nowrap;
  }
  .address { left: 74px; top: 150px; }
  .contact { left: 300px; top: 175px; }
  .contact .person {
    color: var(--text-dark);
    font-size: 16px;
    line-height: 24px;
  }

  .card-bands {
    position: absolute;
    left: 0; bottom: 0;
    width: 580px; height: 120px;
  }
</style>
</head>
<body>

  <section class="card card--back" aria-label="Business card, contact side">
    <div class="brand-name"><span class="brand-dot"></span>Ferncrest Dental, LLC</div>
    <address class="address">
      2871 Marlowe Street,<br>
      Bethlehem, PA 18093.
    </address>
    <div class="contact">
      <div class="person">Dr. Lorna Pettigrew</div>
      <div>610-555-0193</div>
      <div>ferncrestdental.office@examplemail.test</div>
    </div>
    <svg class="card-bands" viewBox="0 0 580 120" preserveAspectRatio="none" aria-hidden="true">
      <path d="M0 70 C 250 60, 450 80, 580 120 L 0 120 Z" fill="var(--green-light)"/>
      <path d="M0 55 C 250 40, 460 65, 580 120 C 450 80, 250 60, 0 70 Z" fill="var(--green-dark)"/>
    </svg>
  </section>

  <section class="card card--front" aria-label="Business card, logo side">
    <div class="brand-name"><span class="brand-dot"></span>Ferncrest Dental, LLC</div>
  </section>

</body>
</html>
```